International Marketing Company - Web Design Project

vLumo is a well-funded start up in London developing an Online Marketing Platform for small businesses in Europe.

We require a large number of high quality business web designs for our business website builder. Our business websites are completely integrated into our Online Marketing systems and therefore it is important for designers to comply with our Design Guidelines.

This initial contest is a trial for us to open up the design process to top designers for the Builders vertical (e.g. Builders, Electricians, Plumbers, Flooring, etc.). We have implemented a base html structure and design and included them in the files.

Use your creativity to design new and fresh designs based on the included elements (e.g. testimonials, business description, etc).

We will award the stated prize money for the top three designs.

Any designers that submit designs we feel are of a high enough quality but do not make the top 3 could still be compensated and WILL be invited to participate in our next vertical competition.

Therefore, we encourage designers to submit as many designs as possible as we may award up to 25 designs.

Submissions will be reviewed daily and feedback provided where possible.

Designers who can also code will have the options to implement their designs for an additional fee.

Good luck!
Updates

There has been a mistake made in regard to the prize. Pixel Harbor should have it fixed soon.

1st place = £350
2nd place = £250
3rd Place = £150

Thanks,
Rowan
25/11/2011

UPDATE:

1st place will win £350
2nd place will win £250
3rd place will win £150

Everything else is as to the specification.

Thanks
Rowan

Target Market(s)

Builders, Electricians, Plumbers, Tradesman, Small construction companies

Industry/Entity Type

Business

Requirements
Must have
• Totally new designs based around the elements we want to show on each page.

We are looking for something different to the design we already have. But you can use that as a starting point.

Use the included files to see what is required for each page. Here is a brief outline:

Homepage - Testimonials, News, Business Description, Latest Projects and Call to action

About-Us - Team Summary, About the Business and a call to action

Projects Page - Project Details (Oage Title and description), Each project needs a title, content and 2 images.

Testimonials Page - The testifiers name and their comment

Contacts Page - Trelwyn Map, Company address, business hours, contact form and a call to action.

Please submit final designs in Photoshop or Fireworks format.

Each page has a set of elements. These element must feature in the design of that page. See supporting documents for page details.

All elements must be included in your design. Please do not add any extra element.

Professional look and feel
Nice to have
• Design variations:
Full width designs
Boxed Designs
With AND without carousels
OR static images
Good use of stock images.

Creative use of the elements, dont be restricted/influenced by the default design we have already

Designs based on the 960 grid

```html
<!DOCTYPE html>
<html lang="en">
<head>
<meta charset="utf-8">
<title>Ashgrove Homes – Builders in Crawley</title>
<link rel="stylesheet" href="https://fonts.googleapis.com/css2?family=Open+Sans:ital,wght@0,400;0,600;0,700;1,400&family=Arimo:wght@400;700&display=swap">
<style>
:root{
  --ink:#2b2b2b;
  --text:#333;
  --muted:#7a7a7a;
  --heading-grey:#666;
  --panel:#eeece8;
  --nav:#262626;
  --orange:#f26b1d;
  --white:#fff;
  --footer:#2c2c2c;
  --footer-deep:#1a1a1a;
  --yellow-top:#ffd83a;
  --yellow-bottom:#e0a800;
}
*{box-sizing:border-box;margin:0;padding:0}
html,body{width:776px;height:1200px;overflow:hidden;background:var(--white)}
body{position:relative;font-family:"Arimo",Arial,sans-serif;color:var(--text)}
.abs{position:absolute}

/* Brand */
.brand{left:30px;top:32px;display:flex;align-items:center;gap:8px}
.brand-mark{width:66px;height:70px;background:var(--ink)}
.brand-name{font-family:"Open Sans",sans-serif;font-weight:700;font-size:26px;line-height:28px;color:#3a302d;width:140px;text-transform:uppercase}

/* Navigation */
.main-nav{left:16px;top:124px;width:742px;height:28px;background:linear-gradient(#3a3a3a,var(--nav));border-radius:5px;box-shadow:0 2px 3px rgba(0,0,0,.3)}
.main-nav a{position:absolute;top:0;height:28px;line-height:28px;color:var(--white);font-size:13px;font-weight:700;text-decoration:none;letter-spacing:.2px}
.main-nav a.active{left:0;width:75px;text-align:center;background:linear-gradient(#a9a9a9,#7d7d7d);border-radius:5px 0 0 5px}
.search{position:absolute;left:550px;top:4px;width:170px;height:20px;border-radius:3px;background:var(--white);overflow:hidden}
.search span{position:absolute;left:26px;top:4px;font-size:9px;font-style:italic;color:#333}
.search svg{position:absolute;left:6px;top:4px}
.search-btn{position:absolute;right:0;top:0;width:20px;height:20px;background:var(--orange)}

/* Hero */
.hero{left:16px;top:174px;width:742px;height:291px;background:var(--panel);border-radius:5px}
.hero-title{left:38px;top:202px;font-family:"Open Sans",sans-serif;font-size:38px;color:#222;letter-spacing:-.5px}
.hero-text{left:43px;top:255px;width:245px;font-size:10.5px;line-height:13px;color:#555}
.btn-more{left:42px;top:376px;width:128px;height:19px;border-radius:3px;background:#adadad;color:var(--white);font-size:12px;text-align:center;line-height:19px}
.dismiss{left:182px;top:376px;display:flex;align-items:center;gap:7px;font-family:"Open Sans",sans-serif;font-style:italic;font-size:10px;color:#222}
.dismiss i{width:19px;height:19px;border-radius:50%;background:#adadad;color:var(--white);font-style:normal;font-size:10px;text-align:center;line-height:19px}
.hero-photo{left:307px;top:220px;width:435px;height:212px;background:linear-gradient(120deg,#d9b64a 0%,#8a5a2e 35%,#3a2c22 60%,#c9c3b8 85%,#f2f2f2 100%);box-shadow:0 8px 10px -6px rgba(0,0,0,.45)}
.arrow{width:22px;height:22px;background:#111;border-radius:2px;display:flex;align-items:center;justify-content:center}
.arrow.light{background:var(--white);border:1px solid #ccc}

/* Headings */
.section-title{font-family:"Open Sans",sans-serif;font-weight:600;font-size:18px;color:#1a1a1a}
.section-rule{height:2px;background:var(--ink)}
.side-title{font-family:"Open Sans",sans-serif;font-weight:700;font-size:13.5px;color:var(--heading-grey)}
.side-rule{height:2px;background:#555}

/* Welcome */
.welcome{left:16px;top:532px;width:462px;font-size:10.5px;line-height:14.6px;color:var(--text)}
.welcome p{margin-bottom:14.6px}
.more{color:var(--orange)}
.cta{left:18px;top:700px;width:142px;height:75px;border-radius:5px;background:linear-gradient(var(--yellow-top),var(--yellow-bottom));box-shadow:0 6px 8px -4px rgba(0,0,0,.4);font-family:"Open Sans",sans-serif;font-weight:700;font-size:17px;line-height:20px;color:#2a2200;text-align:center;padding-top:8px}

/* Projects */
.projects{left:16px;top:841px;width:465px;height:164px;background:var(--ink);box-shadow:0 8px 10px -6px rgba(0,0,0,.5)}
.project{position:absolute;top:11px;width:100px}
.project-photo{width:100px;height:100px;border:1px solid #ddd}
.project-name{margin-top:12px;font-size:8px;line-height:11px;color:var(--white);text-align:center}

/* Testimonials side */
.quote{left:511px;width:235px}
.quote-text{padding-left:15px;font-size:8.2px;line-height:11.4px;color:var(--text);position:relative}
.quote-text::before{content:"\201C";position:absolute;left:0;top:-4px;font-family:Georgia,serif;font-size:18px;color:var(--orange);font-weight:700}
.quote-name{padding-left:15px;margin-top:14px;font-size:8.5px;color:var(--muted)}

/* News */
.news{left:511px;width:235px;display:flex;gap:5px;font-size:8.2px;line-height:11.4px}
.news svg{flex:none;margin-top:1px}

/* Footer */
.footer{left:0;top:1072px;width:776px;height:128px;background:linear-gradient(#3a3a3a,var(--footer) 40%,var(--footer-deep))}
.footer-scene{left:365px;top:965px;width:411px;height:210px;background:radial-gradient(ellipse at 55% 70%,rgba(196,160,110,.75),rgba(120,120,120,.45) 55%,rgba(255,255,255,0) 75%)}
.social{top:1103px;width:46px;height:36px;border-radius:8px;background:linear-gradient(#4ea7e8,#1d5fa8);box-shadow:0 3px 4px rgba(0,0,0,.5)}
.footer-bar{left:0;top:1178px;width:776px;height:22px;background:#151515;font-size:8px;color:#ddd}
.footer-bar .copy{position:absolute;left:18px;top:7px}
.footer-bar .links{position:absolute;right:18px;top:7px}
</style>
</head>
<body>

<header>
  <div class="abs brand">
    <div class="brand-mark"></div>
    <div class="brand-name">Ashgrove Homes</div>
  </div>
  <nav class="abs main-nav">
    <a class="active" href="#">HOME</a>
    <a href="#" style="left:86px">ABOUT US</a>
    <a href="#" style="left:175px">TESTIMONIALS</a>
    <a href="#" style="left:291px">PORTFOLIO</a>
    <a href="#" style="left:387px">CONTACTS</a>
    <div class="search">
      <svg width="11" height="11" viewBox="0 0 11 11"><circle cx="4.5" cy="4.5" r="3.3" fill="none" stroke="#111" stroke-width="1.6"/><line x1="7" y1="7" x2="10" y2="10" stroke="#111" stroke-width="1.8"/></svg>
      <span>Search......</span>
      <div class="search-btn"><svg width="20" height="20" viewBox="0 0 20 20"><path d="M8 5l5 5-5 5" fill="none" stroke="#fff" stroke-width="2.2"/></svg></div>
    </div>
  </nav>
</header>

<section>
  <div class="abs hero"></div>
  <h1 class="abs hero-title">Testimonials</h1>
  <p class="abs hero-text">Kestrel Build are the best buildres in Crawley. They are experts in all areas of house building and i am extremely saris fied with mynew loft convesion.</p>
  <div class="abs btn-more">Find Out More....</div>
  <div class="abs dismiss"><i>×</i>Don't show again</div>
  <div class="abs hero-photo" role="img" aria-label="Tool belt with spirit level, hammer, pliers, gloves and a white hard hat"></div>
  <div class="abs arrow" style="left:297px;top:323px"><svg width="10" height="12" viewBox="0 0 10 12"><path d="M7 1L2 6l5 5" fill="none" stroke="#fff" stroke-width="2"/></svg></div>
  <div class="abs arrow" style="left:726px;top:323px"><svg width="10" height="12" viewBox="0 0 10 12"><path d="M3 1l5 5-5 5" fill="none" stroke="#fff" stroke-width="2"/></svg></div>
</section>

<main>
  <h2 class="abs section-title" style="left:16px;top:488px">Welcome to Kestrel Buildres</h2>
  <div class="abs section-rule" style="left:16px;top:513px;width:465px"></div>
  <div class="abs welcome">
    <p>I am an experienced builder in Crawley, Kestrel Build have been based in Crawley for over 10 years. My team and I are proven, reliable builders based in Crawley. We've come across a lot in our time, so don't hesitate to get in touch about any building job in Crawley.</p>
    <p>I am a friendly, handyman who has built a team of excellent tradesmen based in Crawley. My builders in Crawley have years of experience in kitchen renovation, bathroom renovation, roofing and plumbing, loft conversions and house restoration.</p>
    <p>Call Kestrel Build on 0100555019 now to discuss how we can help you. My quotes are always FREE with no obligation. <span class="more">more &gt;&gt;</span></p>
  </div>
  <div class="abs cta">Contact US<br>for a<br>Quote Now</div>

  <h2 class="abs section-title" style="left:16px;top:798px">Latest Projects</h2>
  <div class="abs section-rule" style="left:16px;top:822px;width:465px"></div>
  <div class="abs projects">
    <div class="project" style="left:20px"><div class="project-photo" role="img" aria-label="Restored living room with sofa and coffee table" style="background:linear-gradient(#e6e2da,#8b7f72)"></div><div class="project-name">House restoration in Crawley</div></div>
    <div class="project" style="left:129px"><div class="project-photo" role="img" aria-label="Loft conversion lounge with white chairs and wall shelves" style="background:linear-gradient(#efe9de,#c9bba3)"></div><div class="project-name">Loft conversion near Crawley</div></div>
    <div class="project" style="left:238px"><div class="project-photo" role="img" aria-label="Freshly painted living room with dark feature wall" style="background:linear-gradient(#f2f2f2,#5a5a5a)"></div><div class="project-name">Home painting &amp; Decorating in Crawley</div></div>
    <div class="project" style="left:347px"><div class="project-photo" role="img" aria-label="House extension bedroom with warm lighting" style="background:linear-gradient(#8c93a8,#3c2e2a)"></div><div class="project-name">Beautiful house extension in Crawley</div></div>
    <div class="abs arrow light" style="left:7px;top:48px"><svg width="10" height="12" viewBox="0 0 10 12"><path d="M7 1L2 6l5 5" fill="none" stroke="#111" stroke-width="2"/></svg></div>
    <div class="abs arrow light" style="left:440px;top:48px"><svg width="10" height="12" viewBox="0 0 10 12"><path d="M3 1l5 5-5 5" fill="none" stroke="#111" stroke-width="2"/></svg></div>
  </div>
</main>

<aside>
  <h3 class="abs side-title" style="left:511px;top:491px">CUSTOMERS SAY...</h3>
  <div class="abs side-rule" style="left:511px;top:513px;width:247px"></div>

  <div class="abs quote" style="top:532px">
    <p class="quote-text">Kestrel Build are the best builders in Crawley. They are experts in all areas of house building and I am extremely satisfied with my new loft conversion.<br><span class="more">more &gt;&gt;</span></p>
    <p class="quote-name">Mr. Halvorsen</p>
  </div>
  <div class="abs quote" style="top:612px">
    <p class="quote-text">I rarely write references for anyone, but Kestrel Build builders in Crawley are outstanding. They restored my Crawley home to a very high specification and the team are very approachable and friendly.<br><span class="more">more &gt;&gt;</span></p>
    <p class="quote-name">Mr. Halvorsen</p>
  </div>
  <div class="abs quote" style="top:703px">
    <p class="quote-text">"I found Kestrel Build in Crawley through their amazing website and I made my decision to ask for a quote once I saw the excellent testimonials. It can be very difficult to find great builders in Crawley but Kestrel Build's team delivers.<br><span class="more">more &gt;&gt;</span></p>
    <p class="quote-name">Mr. Halvorsen</p>
  </div>

  <h3 class="abs side-title" style="left:511px;top:801px">Latest News :</h3>
  <div class="abs side-rule" style="left:511px;top:822px;width:247px"></div>

  <div class="abs news" style="top:840px"><svg width="11" height="10" viewBox="0 0 11 10"><path d="M1 3h3l5-3v10L4 7H1z" fill="#f26b1d"/></svg><p>Kestrel Build have just finished another fine job in Crawley. <span class="more">&nbsp;more &gt;&gt;</span></p></div>
  <div class="abs news" style="top:874px"><svg width="11" height="10" viewBox="0 0 11 10"><path d="M1 3h3l5-3v10L4 7H1z" fill="#f26b1d"/></svg><p>Timber frames seem to be all the rage in London.<br>Using the latest in wood tech! <span class="more">&nbsp;more &gt;&gt;</span></p></div>
  <div class="abs news" style="top:908px"><svg width="11" height="10" viewBox="0 0 11 10"><path d="M1 3h3l5-3v10L4 7H1z" fill="#f26b1d"/></svg><p>Just started a 12th century flat conversion.<br>Lots of great finds! <span class="more">&nbsp;more &gt;&gt;</span></p></div>
</aside>

<footer>
  <div class="abs footer"></div>
  <div class="abs footer-scene" role="img" aria-label="Timber house frame, step ladder, toolbox and builder's tools"></div>
  <div class="abs social" style="left:32px" aria-label="Professional network"></div>
  <div class="abs social" style="left:86px" aria-label="Microblog"></div>
  <div class="abs social" style="left:140px" aria-label="Social network"></div>
  <div class="abs footer-bar">
    <span class="copy">Copyright 2012 Ashgrove Homes All Rights Reserved</span>
    <span class="links">Home | Contact | RSS</span>
  </div>
</footer>

</body>
</html>
```